Bruntel general construction

We need an website that are similar to these websites:
https://www.morvexa.com/en/
https://dulnari.com/company/

but with a tweak. Do not copy the entire website but atleast similar and yet better than them.

For reference this our current website.
https://bruntel.ph/

For the winning Designer please help us with the migration from our old website to the new redesign website.

```html
<!DOCTYPE html>
<html lang="en">
<head>
<meta charset="utf-8">
<title>Bruntel — One Step Ahead in Industrial Services</title>
<link rel="stylesheet" href="https://fonts.googleapis.com/css2?family=Roboto:wght@400;500;700;900&family=Montserrat:wght@300;400&display=swap">
<style>
  :root {
    --ink: #0b0b0b;
    --bar: #0d0d0d;
    --menu: #111111;
    --menu-line: #262626;
    --white: #ffffff;
    --muted: #9a9a9a;
    --red: #c8102e;
    --orange-panel: rgba(196, 98, 40, 0.72);
    --panel-text: rgba(235, 225, 215, 0.72);
    --seg-1: #1f86c4;
    --seg-2: #0f5a8e;
    --seg-3: #d35a1e;
    --seg-4: #e09a18;
    --seg-5: #d4b012;
    --logo: #f39a1d;
  }
  * { margin: 0; padding: 0; box-sizing: border-box; }
  html, body { width: 1200px; height: 546px; overflow: hidden; background: var(--ink); }
  body { font-family: "Roboto", Arial, sans-serif; color: var(--white); }

  .page { position: relative; width: 1200px; height: 546px; overflow: hidden; }

  .hero-photo {
    position: absolute; left: 0; top: 66px; width: 1200px; height: 480px;
    background:
      radial-gradient(ellipse 260px 170px at 1000px 420px, #b9b6b0 0%, rgba(185,182,176,0) 100%),
      radial-gradient(ellipse 420px 200px at 700px 470px, #8e8170 0%, rgba(142,129,112,0) 100%),
      linear-gradient(180deg, #4d4f55 0%, #5a5650 40%, #6e5f4c 62%, #5c554c 100%);
  }

  .site-header {
    position: absolute; left: 0; top: 0; width: 1200px; height: 66px;
    background: var(--bar);
  }
  .brand {
    position: absolute; left: 22px; top: 22px;
    display: flex; align-items: center; gap: 6px;
    font-family: "Roboto", Arial, sans-serif; font-weight: 700; font-size: 13px;
    color: var(--logo); letter-spacing: 0.5px;
  }
  .brand-dot { width: 10px; height: 10px; border-radius: 50%; background: var(--logo); }

  .main-nav a {
    position: absolute; top: 23px;
    font-size: 12.5px; font-weight: 700; letter-spacing: 0.6px;
    color: #e6e6e6; text-decoration: none; text-transform: uppercase;
  }
  .main-nav a.is-current { color: var(--white); }
  .nav-underline { position: absolute; top: 62px; height: 2px; background: var(--red); }

  .theme-label { position: absolute; left: 979px; top: 24px; font-size: 12px; color: var(--muted); letter-spacing: 0.6px; }
  .theme-toggle {
    position: absolute; left: 1040px; top: 15px; width: 31px; height: 31px;
    border-radius: 50%; border: 1px solid #2a2a2a; display: flex; align-items: center; justify-content: center;
  }
  .header-cta {
    position: absolute; left: 1085px; top: 14px; width: 89px; height: 33px;
    border: 1px solid #2e2e2e; display: flex; align-items: center; justify-content: center;
    font-size: 11.5px; font-weight: 700; letter-spacing: 0.6px; color: var(--white);
  }

  .intro-panel {
    position: absolute; left: 68px; top: 127px; width: 458px; height: 388px;
    background: var(--orange-panel); border-radius: 6px;
  }
  .intro-text {
    position: absolute; left: 0; top: 58px; width: 458px;
    font-family: "Montserrat", Arial, sans-serif; font-weight: 300;
    font-size: 26px; line-height: 32px; text-align: center; color: var(--panel-text);
  }

  .hero-title {
    position: absolute; right: 464px; top: 186px;
    font-family: "Roboto", Arial, sans-serif; font-weight: 900; font-size: 58px; letter-spacing: -0.5px;
    color: var(--white);
  }
  .hero-tagline {
    position: absolute; left: 429px; top: 272px;
    font-size: 20px; font-weight: 400; color: var(--white);
  }
  .hero-button {
    position: absolute; left: 476px; top: 328px; width: 249px; height: 45px;
    background: var(--red); display: flex; align-items: center; justify-content: center;
    font-size: 13px; font-weight: 700; letter-spacing: 1px; color: var(--white);
  }

  .sector-bars span { position: absolute; top: 524px; width: 84px; height: 8px; border-radius: 4px; }
  .slide-dots span {
    position: absolute; top: 521px; width: 10px; height: 10px; border-radius: 50%;
    border: 1.5px solid #e8e8e8;
  }
  .slide-dots span.is-active { background: var(--red); border-color: var(--red); }

  .services-menu {
    position: absolute; left: 376px; top: 64px; width: 214px;
    background: var(--menu); border-top: 2px solid var(--red);
    list-style: none;
  }
  .services-menu li {
    height: 41px; display: flex; align-items: center; padding-left: 19px;
    font-size: 12.5px; font-weight: 500; color: #f0f0f0;
    border-bottom: 1px solid var(--menu-line);
  }
  .services-menu li:last-child { border-bottom: none; }
</style>
</head>
<body>
<div class="page">
  <div class="hero-photo" role="img" aria-label="Construction site with cranes at dusk, rolled blueprints and a white company hard hat"></div>

  <header class="site-header">
    <div class="brand"><span class="brand-dot"></span>BRUNTEL</div>
    <nav class="main-nav">
      <a class="is-current" style="left:233px">Home</a>
      <a style="left:299px">About Us</a>
      <a style="left:391px">Our Services</a>
      <a style="left:509px">Our Team</a>
      <a style="left:603px">News &amp; Media</a>
      <a style="left:723px">Contact Us</a>
    </nav>
    <span class="nav-underline" style="left:233px;width:38px"></span>
    <span class="theme-label">THEME :</span>
    <span class="theme-toggle">
      <svg width="14" height="14" viewBox="0 0 24 24"><path d="M20 14.5A8.5 8.5 0 1 1 9.5 4a7 7 0 0 0 10.5 10.5z" fill="#ffffff"/></svg>
    </span>
    <span class="header-cta">CONTACT</span>
  </header>

  <section class="intro-panel">
    <p class="intro-text">We value the training of<br>our people and ensure<br>our reputation as a<br>leading contractor in the<br>construction, industrial, and<br>oil and gas sectors while<br>providing remarkable support<br>services for repair and<br>maintenance projects.</p>
  </section>

  <h1 class="hero-title">BRUNTEL</h1>
  <p class="hero-tagline">One Step Ahead in Industrial Services</p>
  <span class="hero-button">DISCOVER OUR SERVICES</span>

  <div class="sector-bars">
    <span style="left:68px;background:var(--seg-1)"></span>
    <span style="left:161px;background:var(--seg-2)"></span>
    <span style="left:254px;background:var(--seg-3)"></span>
    <span style="left:347px;background:var(--seg-4)"></span>
    <span style="left:442px;background:var(--seg-5)"></span>
  </div>
  <div class="slide-dots">
    <span style="left:566px"></span>
    <span style="left:586px"></span>
    <span style="left:605px"></span>
    <span class="is-active" style="left:625px"></span>
  </div>

  <ul class="services-menu">
    <li>Environmental Protection</li>
    <li>Power Generation</li>
    <li>Water Treatment</li>
    <li>Construction</li>
    <li>Oil and Gas</li>
  </ul>
</div>
</body>
</html>
```